Investment Advisor E-Newsletter Banner Design

I need a banner designed for an email newsletter that will be sent monthly to clients and prospects. We want to see designs that are elegant and use our logo well. The banner should be 922x150px and should go well with the www.bhtlwest.com website. Should include Logo and email and phone number.

Target Market(s)

High net worth investors

Number of Pages Required

1 page

Requirements
Must have
• logo, place for email (info@bhtlwest.com) and phone number (555-219-0387), colors and design that work well with www.bhtlwest.com website

```html
<!DOCTYPE html>
<html lang="en">
<head>
<meta charset="utf-8">
<title>Beacon Hill Trust – Newsletter Banner</title>
<link rel="stylesheet" href="https://fonts.googleapis.com/css2?family=Tinos:ital,wght@0,400;1,400&family=Arimo:ital@1&display=swap">
<style>
  :root {
    --parchment-light: #d9d6b8;
    --parchment-mid: #b8bfa0;
    --teal-wash: #8fa69a;
    --band-black: #121212;
    --band-edge: #262626;
    --brand-blue: #1c22c4;
    --icon-white: #ffffff;
    --icon-navy: #1b3f8f;
    --text-white: #ffffff;
    --team-dark: #3a3d42;
    --team-light: #9aa0a0;
  }
  html, body {
    margin: 0;
    padding: 0;
    width: 1200px;
    height: 195px;
    overflow: hidden;
    background: #ffffff;
  }
  .banner {
    position: relative;
    width: 1200px;
    height: 195px;
    overflow: hidden;
  }
  .banner__texture {
    position: absolute;
    inset: 0;
    background:
      radial-gradient(ellipse at 20% 40%, var(--parchment-light) 0%, transparent 60%),
      radial-gradient(ellipse at 85% 70%, var(--parchment-light) 0%, transparent 55%),
      linear-gradient(100deg, var(--parchment-mid) 0%, var(--teal-wash) 45%, var(--parchment-mid) 100%);
  }
  .banner__band {
    position: absolute;
    left: 0;
    top: 0;
    width: 1200px;
    height: 195px;
  }
  .banner__team {
    position: absolute;
    right: 0;
    top: 0;
    width: 348px;
    height: 195px;
    background: linear-gradient(90deg, rgba(58,61,66,0) 0%, rgba(58,61,66,0.55) 18%, var(--team-dark) 50%, rgba(154,160,160,0.7) 100%);
  }
  .brand {
    position: absolute;
    left: 40px;
    top: 72px;
    display: flex;
    align-items: center;
    gap: 14px;
  }
  .brand__square {
    width: 40px;
    height: 40px;
    background: var(--brand-blue);
  }
  .brand__name {
    font-family: "Tinos", serif;
    font-weight: 400;
    font-size: 34px;
    color: var(--brand-blue);
    line-height: 1;
    white-space: nowrap;
  }
  .contact {
    position: absolute;
    display: flex;
    align-items: center;
    color: var(--text-white);
    white-space: nowrap;
  }
  .contact--email { left: 528px; top: 44px; }
  .contact--phone { left: 524px; top: 119px; }
  .contact__icon {
    width: 41px;
    height: 41px;
    flex: none;
  }
  .contact__text--email {
    margin-left: 30px;
    font-family: "Tinos", serif;
    font-style: italic;
    font-size: 25px;
  }
  .contact__text--phone {
    margin-left: 25px;
    font-family: "Arimo", sans-serif;
    font-style: italic;
    font-size: 26px;
  }
</style>
</head>
<body>
<div class="banner">
  <div class="banner__texture" role="img" aria-label="Weathered parchment texture in sage and cream tones"></div>

  <svg class="banner__band" viewBox="0 0 1200 195" aria-hidden="true">
    <defs>
      <linearGradient id="bandShade" x1="0" y1="0" x2="1" y2="1">
        <stop offset="0" stop-color="var(--band-black)"/>
        <stop offset="0.6" stop-color="var(--band-edge)"/>
        <stop offset="1" stop-color="var(--band-black)"/>
      </linearGradient>
    </defs>
    <polygon points="495,0 866,0 781,195 414,195" fill="url(#bandShade)"/>
  </svg>

  <div class="banner__team" role="img" aria-label="Photograph of a group of business professionals in suits"></div>

  <div class="brand">
    <div class="brand__square"></div>
    <div class="brand__name">Beacon Hill Trust, Ltd.</div>
  </div>

  <div class="contact contact--email">
    <svg class="contact__icon" viewBox="0 0 40 40" aria-hidden="true">
      <circle cx="20" cy="20" r="20" fill="var(--icon-white)"/>
      <rect x="10" y="13" width="20" height="14" fill="var(--icon-navy)"/>
      <polyline points="10,13 20,21 30,13" fill="none" stroke="var(--icon-white)" stroke-width="1.6"/>
    </svg>
    <span class="contact__text contact__text--email">info@bhtlwest.com</span>
  </div>

  <div class="contact contact--phone">
    <svg class="contact__icon" viewBox="0 0 40 40" aria-hidden="true">
      <circle cx="20" cy="20" r="20" fill="var(--icon-white)"/>
      <path d="M14.5 10.5c1-.6 2-.3 2.5.6l1.7 3.2c.4.8.2 1.7-.5 2.2l-1.3 1c.9 2.3 2.6 4.1 4.9 5.1l1-1.3c.5-.7 1.5-.9 2.2-.5l3.2 1.7c.9.5 1.2 1.5.6 2.5l-1 1.7c-.6 1-1.8 1.5-2.9 1.2C18.2 26.4 13.6 21.8 12 15.1c-.3-1.1.2-2.3 1.2-2.9z" fill="var(--icon-navy)"/>
    </svg>
    <span class="contact__text contact__text--phone">555-219-0387</span>
  </div>
</div>
</body>
</html>
```